Fast growing Tech company needs redesign of Varnith's end user website!

We need to have our login screen, the dashboard, and the one page of the Varnith site to be redesigned for the end-users. Varnith is a document hosting service for title companies and real estate law firms. This allows the buyers and sellers to view their closing documents after closing along with many other features that help them out during the closing of their property. More information about what we do can be found on our test site https://qpx.482.sampledrafthost.example/. PLEASE NOTE: THE ABOVE SITE IS NOT THE ONE WE NEED REDONE. The above site is our corporate site that explains our service offering and we thought it would be helpful in providing you a better understanding of our service.
The site that we want to have redesigned is for the end user. THE SITE THAT NEEDS TO BE REDONE ARE THE SCREENSHOTS ATTACHED. We will need the login screen, dashboard, and the one page redesigned.
.
We will just need this in HTML and we will then do the rest for the placeholders for logos, data, mapping etc.
Overall, we want a new, fresh, and modern look for the website and we want the login screen, dashboard and one page website to be consistent in design. Again, these are the three screenshots that are attached.
For the winner, we will most likely need to hire you again for more sites because we have other versions.
Thank you and if any questions, please let us know.
Target Market(s)
This site is for buyer and sellers during the closing process of real estate transaction.

```html
<!DOCTYPE html>
<html lang="en">
<head>
<meta charset="utf-8">
<title>Varnith – Buyer Portal</title>
<link rel="stylesheet" href="https://fonts.googleapis.com/css2?family=Poppins:wght@400;500;600&family=Raleway:wght@400;700&family=Roboto+Slab:wght@500;600&display=swap">
<style>
:root{
  --brand:#33a5d8;
  --brand-strong:#2196f3;
  --accent:#2a9fd6;
  --ink:#4a4a55;
  --ink-soft:#666;
  --line:#bfe3f7;
  --done:#1ed40f;
  --partial:#f2f500;
  --todo:#ff0f0f;
  --active:#a97ee8;
  --map-land:#c9d9c6;
  --map-water:#86a8e6;
  --paper:#fff;
}
*{margin:0;padding:0;box-sizing:border-box}
html,body{width:734px;height:1200px;overflow:hidden;background:var(--paper)}
body{position:relative;font-family:'Poppins',sans-serif;color:var(--ink)}
.abs{position:absolute}
.client-header{left:54px;top:0;width:628px;height:51px;border:1px solid var(--line);display:flex;align-items:center;justify-content:center}
.client-name{font-family:'Poppins',sans-serif;font-weight:600;font-size:15px;letter-spacing:4px;color:var(--ink)}
.sidebar{left:54px;top:51px;width:99px;height:1149px;background:var(--brand)}
.side-brand{left:14px;top:4px;color:#fff;font-size:12px;font-weight:400}
.side-tag{left:13px;top:22px;color:#e6f5ff;font-size:3.5px}
.side-rule{left:0;top:27px;width:99px;height:1px;background:rgba(255,255,255,.25)}
.nav{list-style:none}
.nav li{position:absolute;left:9px;display:flex;align-items:center;gap:4px;color:#fff;font-size:5.2px;white-space:nowrap}
.nav svg{width:6px;height:6px}
.nav .active::before{content:"";position:absolute;left:-9px;top:-7px;width:2px;height:20px;background:var(--active)}
.side-mark{left:6px;top:1104px;color:#fff;font-size:21px;font-weight:400;letter-spacing:-.5px}
.side-copy{left:29px;top:1138px;color:#fff;font-size:5px}
.welcome{left:153px;top:56px;width:529px;text-align:center;font-family:'Roboto Slab',serif;font-weight:500;font-size:9.5px;color:var(--ink-soft)}
.intro{left:156px;top:72px;width:522px;text-align:center;font-size:5.6px;line-height:8.8px;color:var(--ink-soft)}
.divider{left:169px;width:500px;height:1px;border-top:1px dotted #777}
.divider-badge{width:18px;height:18px;border-radius:50%;background:#fff;border:1px solid #eee;display:flex;align-items:center;justify-content:center}
.section-title{left:153px;width:425px;text-align:center;font-family:'Roboto Slab',serif;font-weight:600;font-size:7.8px;color:var(--accent)}
.info-head{font-family:'Raleway',sans-serif;font-weight:700;font-size:8.8px;color:var(--ink-soft)}
.info-line{font-family:'Raleway',sans-serif;font-size:9.3px;color:var(--ink-soft);white-space:nowrap}
.map{left:371px;top:146px;width:311px;height:222px;background:linear-gradient(100deg,var(--map-land) 0%,#dcdcd6 45%,var(--map-water) 70%,var(--map-water) 100%)}
.tier{font-weight:600;font-size:7px;color:var(--ink)}
.bar{left:256px;width:414px;height:3px;border-radius:2px}
.step{font-weight:500;font-size:6.2px;color:var(--ink);white-space:nowrap}
.sub-head{font-weight:600;font-size:7.5px;color:var(--ink)}
.doc{display:flex;align-items:center;gap:8px;left:219px;font-weight:500;font-size:6.2px;color:var(--ink)}
.wire-row{left:494px;width:176px;height:19px;display:flex;border:1px solid var(--line)}
.wire-label{width:38px;background:var(--brand-strong);color:#fff;font-size:3.4px;font-weight:600;display:flex;align-items:center;justify-content:center;text-align:center}
.wire-input{flex:1;padding-left:7px;display:flex;align-items:center;font-size:5px;color:#b8dcf5}
.submit{left:571px;top:945px;width:60px;height:18px;background:var(--brand-strong);color:#fff;font-size:3.6px;font-weight:600;display:flex;align-items:center;justify-content:center;border-radius:1px}
.footer{left:153px;top:1152px;width:529px;height:48px;background:var(--brand)}
.foot-link{top:17px;color:#fff;font-size:5.4px}
.foot-dot{top:38px;width:5px;height:5px;border:1px solid #fff;border-radius:50%}
</style>
</head>
<body>
<header class="abs client-header"><span class="client-name">CLIENTLOGO</span></header>

<aside class="abs sidebar">
  <span class="abs side-brand">varnith</span>
  <span class="abs side-tag">staying in the loop</span>
  <span class="abs side-rule"></span>
  <ul class="nav">
    <li style="top:35px"><svg viewBox="0 0 10 10"><path d="M1 5L5 1.5 9 5v4H6V6.5H4V9H1z" fill="none" stroke="#fff"/></svg>Home</li>
    <li style="top:58px"><svg viewBox="0 0 10 10"><path d="M1 9h1.6V6H1zM4 9h1.6V2H4zM7 9h1.6V4.5H7z" fill="#fff"/></svg>Dashboard</li>
    <li class="active" style="top:81px"><svg viewBox="0 0 10 10"><rect x="1" y="2" width="8" height="6" fill="none" stroke="#fff"/><path d="M1 2l4 3 4-3" fill="none" stroke="#fff"/></svg>Transactions</li>
    <li style="top:103px"><svg viewBox="0 0 10 10"><path d="M1 2v6M3 2v6M4.5 2v6M6.5 2v6M8.5 2v6" stroke="#fff" stroke-width="1.1"/></svg>Milestones</li>
    <li style="top:126px"><svg viewBox="0 0 10 10"><rect x="1.5" y="1" width="7" height="8" fill="#fff"/><path d="M3 4h4M3 6h4" stroke="#33a5d8"/></svg>Documents and Wire Details</li>
    <li style="top:148px"><svg viewBox="0 0 10 10"><circle cx="5" cy="3.2" r="2" fill="none" stroke="#fff"/><path d="M1.5 9c0-2.5 7-2.5 7 0" fill="none" stroke="#fff"/></svg>Parties to Transaction</li>
    <li style="top:171px"><svg viewBox="0 0 10 10"><path d="M1 2h6v4H3L1 8z" fill="#fff"/><path d="M8 4h1v5l-2-1.5H4" fill="none" stroke="#fff"/></svg>Moving Checklist and Wishlist</li>
    <li style="top:193px"><svg viewBox="0 0 10 10"><rect x="1" y="2" width="8" height="7" fill="none" stroke="#fff"/><path d="M1 4h8M3 1v2M7 1v2" stroke="#fff"/></svg>Address/Coupon Change</li>
    <li style="top:216px"><svg viewBox="0 0 10 10"><circle cx="5" cy="5" r="4" fill="none" stroke="#fff"/><path d="M1 5h8M5 1c-2 2.5-2 5.5 0 8M5 1c2 2.5 2 5.5 0 8" fill="none" stroke="#fff" stroke-width=".7"/></svg>Frequently Asked Questions</li>
    <li style="top:239px"><svg viewBox="0 0 10 10"><circle cx="5" cy="5" r="3" fill="none" stroke="#fff" stroke-width="2" stroke-dasharray="1.5 1"/><circle cx="5" cy="5" r="1" fill="#fff"/></svg>Settings</li>
  </ul>
  <span class="abs side-mark">varnith</span>
  <span class="abs side-copy">VARNITH® 2021</span>
</aside>

<main>
  <h1 class="abs welcome">WELCOME CLARK BUYER</h1>
  <p class="abs intro">On behalf of all of us at The Real Estate Law Firm, we would like to thank you for choosing us for the closing of your property. Because we want you to be informed at every step of the process, we use the innovative Digital Closing Package to keep all parties involved in the transaction on the same page for a smooth and successful closing.</p>

  <div class="abs divider" style="top:101px"></div>
  <div class="abs divider-badge" style="left:359px;top:92px"><svg width="8" height="8" viewBox="0 0 10 10"><path d="M5 1v8M2 6l3 3 3-3" fill="none" stroke="#2196f3"/></svg></div>
  <h2 class="abs section-title" style="top:115px;left:153px;width:425px">MY TRANSACTIONS</h2>

  <div class="abs info-head" style="left:165px;top:147px">YOUR TRANSACTION INFORMATION</div>
  <div class="abs info-line" style="left:165px;top:161px">File Number: 2018-015987</div>
  <div class="abs info-line" style="left:165px;top:174px">Buyer: Clark Buyer</div>
  <div class="abs info-line" style="left:165px;top:188px">Seller: Chloe Seller</div>
  <div class="abs info-line" style="left:165px;top:201px">Agent: Bob Buyer Agent</div>

  <div class="abs info-head" style="left:165px;top:254px">PROPERTY ADDRESS</div>
  <div class="abs info-line" style="left:165px;top:268px">2400 Back Street</div>
  <div class="abs info-line" style="left:165px;top:281px">Miami, FL 33155</div>

  <div class="abs info-head" style="left:165px;top:321px">PURCHASE DETAILS</div>
  <div class="abs info-line" style="left:165px;top:335px">Purchase Price: USD$ 580,000</div>
  <div class="abs info-line" style="left:165px;top:349px">Settlement Date: Tue, Dec 25 2018</div>

  <div class="abs map" role="img" aria-label="Map showing the property location"></div>

  <div class="abs divider" style="top:399px"></div>
  <div class="abs divider-badge" style="left:359px;top:390px"><svg width="8" height="8" viewBox="0 0 10 10"><path d="M5 1v8M2 6l3 3 3-3" fill="none" stroke="#2196f3"/></svg></div>
  <h2 class="abs section-title" style="top:420px;left:153px;width:415px">CLOSING MILESTONES</h2>

  <div class="abs tier" style="left:165px;top:474px">COMPLETED</div>
  <div class="abs bar" style="top:478px;background:var(--done)"></div>
  <div class="abs step" style="left:256px;top:485px">TRANSACTION STARTED</div>
  <div class="abs step" style="left:340px;top:500px">EARNEST MONEY RECEIVED</div>

  <div class="abs tier" style="left:165px;top:558px">PARTIALLY COMPLETE</div>
  <div class="abs bar" style="top:562px;background:var(--partial)"></div>

  <div class="abs tier" style="left:165px;top:634px">NOT COMPLETE</div>
  <div class="abs bar" style="top:637px;background:var(--todo)"></div>
  <div class="abs step" style="left:251px;top:652px">DELIVERED TITLE REPORT</div>
  <div class="abs step" style="left:340px;top:677px">TITLE CLEARED</div>
  <div class="abs step" style="left:395px;top:698px">SIGNING SCHEDULED</div>
  <div class="abs step" style="left:469px;top:718px">TRANSACTION CLOSED</div>

  <div class="abs divider" style="top:745px"></div>
  <div class="abs divider-badge" style="left:359px;top:736px"><svg width="8" height="8" viewBox="0 0 10 10"><path d="M5 1v8M2 6l3 3 3-3" fill="none" stroke="#2196f3"/></svg></div>
  <h2 class="abs section-title" style="top:755px;left:153px;width:425px">DOCUMENTS &amp; BANK INFORMATION</h2>

  <div class="abs sub-head" style="left:165px;top:771px">DOCUMENTS YOU NEED TO VIEW/DOWNLOAD</div>
  <div class="abs doc" style="top:797px"><svg width="18" height="13" viewBox="0 0 20 14"><path d="M5 13a4 4 0 0 1-.5-8A5.5 5.5 0 0 1 15 4a4.5 4.5 0 0 1 0 9z" fill="#111"/><path d="M10 4.5v6M7.5 8l2.5 2.5L12.5 8" fill="none" stroke="#fff" stroke-width="1.6"/></svg>CLOSING PAPER WORK</div>
  <div class="abs doc" style="top:829px"><svg width="18" height="13" viewBox="0 0 20 14"><path d="M5 13a4 4 0 0 1-.5-8A5.5 5.5 0 0 1 15 4a4.5 4.5 0 0 1 0 9z" fill="#111"/><path d="M10 4.5v6M7.5 8l2.5 2.5L12.5 8" fill="none" stroke="#fff" stroke-width="1.6"/></svg>PURCHASE AGREEMENT</div>
  <div class="abs doc" style="top:862px"><svg width="18" height="13" viewBox="0 0 20 14"><path d="M5 13a4 4 0 0 1-.5-8A5.5 5.5 0 0 1 15 4a4.5 4.5 0 0 1 0 9z" fill="#111"/><path d="M10 4.5v6M7.5 8l2.5 2.5L12.5 8" fill="none" stroke="#fff" stroke-width="1.6"/></svg>DOWNLOAD WIRE INSTRUCTIONS DOCUMENT</div>

  <div class="abs sub-head" style="left:494px;top:771px">WIRING INSTRUCTIONS</div>
  <div class="abs wire-row" style="top:785px"><span class="wire-label">BANK NAME</span><span class="wire-input">Required Field</span></div>
  <div class="abs wire-row" style="top:812px"><span class="wire-label">BANK ADDRESS</span><span class="wire-input">Required Field</span></div>
  <div class="abs wire-row" style="top:839px"><span class="wire-label">BANK PHONE</span><span class="wire-input">Required Field</span></div>
  <div class="abs wire-row" style="top:867px"><span class="wire-label">BANK ABA NUMBER</span><span class="wire-input">Required Field</span></div>
  <div class="abs wire-row" style="top:894px"><span class="wire-label">ACCOUNT NUMBER</span><span class="wire-input">Required Field</span></div>
  <div class="abs wire-row" style="top:921px"><span class="wire-label">OTHER DETAILS</span><span class="wire-input">Required Field</span></div>
  <div class="abs submit">SUBMIT</div>
</main>

<footer class="abs footer">
  <span class="abs foot-link" style="left:65px">HOME</span>
  <span class="abs foot-link" style="left:124px">ABOUT</span>
  <span class="abs foot-link" style="left:181px">PRE-CLOSE</span>
  <span class="abs foot-link" style="left:238px">POST-CLOSE</span>
  <span class="abs foot-link" style="left:290px">GROWTH</span>
  <span class="abs foot-link" style="left:328px">CONTACT US</span>
  <svg class="abs" style="left:503px;top:9px" width="8" height="8" viewBox="0 0 10 10"><path d="M5 9V1M2 4l3-3 3 3" fill="none" stroke="#fff"/></svg>
  <span class="abs foot-dot" style="left:473px"></span>
  <span class="abs foot-dot" style="left:490px"></span>
  <span class="abs foot-dot" style="left:506px"></span>
</footer>
</body>
</html>
```